STAND UP POUCH Package Artwork
Also a $300 bonus may also apply if stellar and timely and save us money on plates / cylinders.
This project is for retail nutritional products in stand up pouches zipper resealable pouches.
This project is for experienced designers for 2 different products in a line that are already in commerce. We want to keep our company branding logo the same, but want to completely redo the look of these two products. if selected for shortlist we will provide a look at what it is now and it needs to be a complete departure from that. Since we are switching from bottles to pouches this is a great time for a complete departure. Art work will be placed on metalized stand up resealable pouches. Knowledge of cylinder use for artwork (these are like plates and are very expensive so would like to hold to no more then 4 cylinders) Therefore creativity with color is paramount. Any and all question will be welcomed and responded to. This is a GO project so selection will be speedy so show us your best stuff when responding. Must be done in all original artwork.
The look for this project is as follows:
1. Elegant look, timeless, minimal colors optimal impact, strong branding, recognizable by site on shelves, clean lines.
DETAILS
1. Please provide samples of your work pertaining to package design and if on pouches even better.
2. Responses to our posting. Generic responses will be ignored, another words, no spam.
3. The artist(s) that are selected for drafts will be provided with further details on the project.
4. Product A: will be on a 191mm x 267mm x 102mm stand up pouch with gusset bottom. This is a single product with two flavors, Chocolate and vanilla. So when designing for this one think of a way to have minimal cylinder changes. This is a high end nutritional vegan shake type product.
5. Product B: will be on a 127mm x 203mm x76mm stand up pouch with gusset bottom. This is a high end weightless type product.
6. Printing templates will be provided for reference, pouch images will be available to see color options of pouches, tag lines, nutritional facts panel, etc…
Some possible elements will be available on our drop box also.
74% female 34-60 36% male 34-60
Retail

```html
<!DOCTYPE html>
<html lang="en">
<head>
<meta charset="utf-8">
<title>Verda Cuisine Pouches</title>
<link rel="stylesheet" href="https://fonts.googleapis.com/css2?family=Cinzel:wght@400;700&family=Open+Sans:wght@400;600&family=Kalam:wght@400&display=swap">
<style>
  :root {
    --bg: #9a9a9a;
    --black: #141212;
    --white: #f7f6f2;
    --green: #7dbb2a;
    --gold: #c9a25a;
    --gold-light: #ecd49a;
    --ink: #4a4440;
    --grey-text: #8a8580;
    --orange: #d98a1e;
    --cream: #efe7d6;
    --choc: #6b3f26;
  }
  * { margin: 0; padding: 0; box-sizing: border-box; }
  html, body { width: 1200px; height: 900px; overflow: hidden; }
  body {
    background: radial-gradient(ellipse at 50% 30%, #c8c8c8, var(--bg));
    position: relative;
    font-family: "Open Sans", sans-serif;
  }
  .pouch {
    position: absolute;
    background: var(--white);
    border-radius: 6px;
    overflow: hidden;
  }
  .pouch--large { left: 160px; top: 170px; width: 470px; height: 620px; }
  .pouch--small { left: 710px; top: 240px; width: 350px; height: 480px; }
  .pouch__art { position: absolute; inset: 0; }
  .pouch > *:not(.pouch__art) { position: absolute; }
  .brand {
    left: 0; right: 0; text-align: center;
    font-family: "Cinzel", serif; color: var(--white);
    letter-spacing: 1px; line-height: 1;
  }
  .brand--large { top: 100px; font-size: 24px; }
  .brand--small { top: 86px; font-size: 19px; }
  .product-name {
    left: 0; right: 0; text-align: center;
    font-family: "Cinzel", serif; font-weight: 700; line-height: 1;
    color: var(--gold-light);
    background: linear-gradient(180deg, var(--gold-light), var(--gold));
    -webkit-background-clip: text; background-clip: text;
    -webkit-text-fill-color: transparent;
  }
  .product-name--large { top: 145px; font-size: 62px; }
  .product-name--small { top: 120px; font-size: 42px; }
  .tagline {
    left: 0; right: 0; top: 230px; text-align: center; line-height: 1;
    font-family: "Kalam", cursive; color: var(--white); font-size: 18px;
  }
  .photo { border-radius: 4px; }
  .photo--vanilla {
    left: 40px; top: 330px; width: 250px; height: 290px;
    background: radial-gradient(ellipse at 50% 40%, #fffdf6, var(--cream) 55%, #d9cdb5);
  }
  .photo--cocoa {
    left: 165px; top: 222px; width: 165px; height: 185px;
    background: radial-gradient(ellipse at 50% 40%, #8a5535, var(--choc) 55%, #3e2416);
  }
  .flavour {
    left: 90px; top: 525px; width: 150px; text-align: center;
    font-family: "Cinzel", serif; font-size: 26px; line-height: 1.05; color: var(--ink);
  }
  .badge-vegan {
    left: 298px; top: 325px; width: 88px; height: 52px;
    background: linear-gradient(135deg, #9bd13e, #4f8f17);
    border-radius: 50% 8px 50% 8px;
    color: #fff; font-family: "Kalam", cursive; font-size: 22px;
    display: flex; align-items: center; justify-content: center;
  }
  .benefits { list-style: none; font-size: 10.5px; color: var(--ink); line-height: 1.45; text-transform: uppercase; }
  .benefits li::before { content: "\25CF"; color: var(--green); margin-right: 6px; font-size: 8px; }
  .benefits--large { left: 282px; top: 405px; }
  .benefits--small { left: 22px; top: 358px; font-size: 9px; width: 140px; }
  .benefits--small li::before { color: var(--orange); }
  .servings { font-size: 13px; color: var(--ink); text-transform: uppercase; }
  .servings--large { left: 300px; top: 508px; width: 160px; border-bottom: 1px solid var(--gold); padding-bottom: 4px; }
  .pack-info { font-size: 8.5px; color: var(--grey-text); text-align: right; line-height: 1.4; }
  .pack-info--large { right: 12px; top: 538px; }
  .calories {
    left: 28px; top: 225px; width: 80px; text-align: center;
    color: var(--gold); font-weight: 600; font-size: 10px; line-height: 1.15;
  }
  .calories__number { display: block; font-size: 34px; line-height: 1; }
  .ribbon {
    left: 160px; top: 388px; width: 180px; height: 32px;
    background: linear-gradient(180deg, #f0a840, var(--orange));
    clip-path: polygon(0 0, 100% 0, 94% 50%, 100% 100%, 0 100%);
    font-family: "Cinzel", serif; font-weight: 700; color: var(--black);
    font-size: 15px; display: flex; align-items: center; padding-left: 20px;
  }
  .servings--small { left: 22px; top: 422px; font-size: 11px; line-height: 1.1; border-bottom: 1px solid var(--gold); padding-bottom: 3px; }
  .servings--small small { display: block; font-size: 7px; }
  .pack-info--small { left: 22px; top: 454px; text-align: left; }
</style>
</head>
<body>
  <section class="pouch pouch--large">
    <svg class="pouch__art" viewBox="0 0 470 620" aria-hidden="true">
      <path d="M0 0H470V288C400 278 330 292 235 318C150 304 80 292 0 302Z" fill="var(--gold)"/>
      <path d="M0 0H470V280C400 270 330 284 235 310C150 296 80 284 0 294Z" fill="var(--green)"/>
      <path d="M0 0H470V270C400 260 330 274 235 300C150 286 80 274 0 284Z" fill="var(--black)"/>
      <line x1="0" y1="30" x2="470" y2="30" stroke="#2d2a28" stroke-width="2"/>
      <line x1="0" y1="38" x2="470" y2="38" stroke="#2d2a28" stroke-width="1"/>
      <line x1="95" y1="220" x2="385" y2="220" stroke="var(--gold)" stroke-width="2"/>
    </svg>
    <div class="brand brand--large">Verda Cuisine</div>
    <h1 class="product-name product-name--large">Harmony</h1>
    <p class="tagline">Luxurious ways for nutrinous days</p>
    <div class="photo photo--vanilla" role="img" aria-label="Vanilla shake splashing in a glass mug with a vanilla flower"></div>
    <p class="flavour">Vanilla Creme</p>
    <div class="badge-vegan">Vegan</div>
    <ul class="benefits benefits--large">
      <li>Full spectrum multi-vitamin</li>
      <li>Phyto nutrients</li>
      <li>Fruits &amp; vegetables</li>
      <li>Organic pea protein</li>
      <li>Pre/pro biotics</li>
    </ul>
    <p class="servings servings--large">Contains 10 servings</p>
    <p class="pack-info pack-info--large">FUNCTIONAL FOOD NUTRITIONAL SHAKE<br>NET WT 1.98 lb (900 G)</p>
  </section>

  <section class="pouch pouch--small">
    <svg class="pouch__art" viewBox="0 0 350 480" aria-hidden="true">
      <path d="M0 0H350V200C280 192 230 204 175 220C110 208 60 200 0 208Z" fill="var(--gold)"/>
      <path d="M0 0H350V192C280 184 230 196 175 212C110 200 60 192 0 200Z" fill="var(--black)"/>
      <line x1="0" y1="24" x2="350" y2="24" stroke="#2d2a28" stroke-width="2"/>
      <line x1="75" y1="172" x2="275" y2="172" stroke="var(--gold)" stroke-width="2"/>
    </svg>
    <div class="brand brand--small">Verda Cuisine</div>
    <h2 class="product-name product-name--small">Slim-Up</h2>
    <div class="photo photo--cocoa" role="img" aria-label="Chocolate pieces splashing into a glass of cocoa shake"></div>
    <p class="calories">ONLY<span class="calories__number">12</span>CALORIES PER SERVING</p>
    <ul class="benefits benefits--small">
      <li>Metabolism booster</li>
      <li>Appetite suppressant</li>
      <li>Fat &amp; sugar free</li>
    </ul>
    <div class="ribbon">Cocoa Charm</div>
    <p class="servings servings--small"><small>Contains</small>30 servings</p>
    <p class="pack-info pack-info--small">NET WT 10.5 oz (300 g)</p>
  </section>
</body>
</html>
```